I would like a stylish low key card that represents my Cedar Lodge. A boutique rental property . This property is of the highest standard and I wish the card to covey this without being old fashion

Industry/Entity Type

Boutique

Contact Information for Business Card

Tess Varlowe
0438207519
tess.varlowe@varlowe.com.au Cedar Lodge

```html
<!DOCTYPE html>
<html lang="en">
<head>
<meta charset="utf-8">
<title>Cedar Lodge — Business Card</title>
<link href="https://fonts.googleapis.com/css2?family=Barlow:wght@300;400;500&display=swap" rel="stylesheet">
<style>
  :root {
    --card-bg: #1f1f1f;
    --pattern-tone: #262626;
    --panel-bg: #151515;
    --title-ink: #d6d6d6;
    --name-ink: #e4e4e4;
    --detail-ink: #bcbcbc;
    --rule-ink: #cfcfcf;
  }
  html, body {
    margin: 0;
    padding: 0;
    width: 1200px;
    height: 741px;
    overflow: hidden;
    background: var(--card-bg);
  }
  .card {
    position: relative;
    width: 1200px;
    height: 741px;
    font-family: "Barlow", "Helvetica Neue", Arial, sans-serif;
    background: var(--card-bg);
  }
  .card__pattern {
    position: absolute;
    inset: 0;
    background: linear-gradient(135deg, var(--pattern-tone) 0%, var(--card-bg) 100%);
  }
  .card__panel {
    position: absolute;
    left: 564px;
    top: 247px;
    width: 539px;
    height: 494px;
    background: var(--panel-bg);
    overflow: hidden;
  }
  .brand-name {
    position: absolute;
    left: 48px;
    top: 48px;
    width: 444px;
    margin: 0;
    font-weight: 300;
    font-size: 84px;
    line-height: 1;
    letter-spacing: -1px;
    color: var(--title-ink);
    white-space: nowrap;
  }
  .contact {
    position: absolute;
    left: 53px;
    top: 318px;
    width: 444px;
  }
  .contact__rule {
    height: 2px;
    background: var(--rule-ink);
    margin-bottom: 34px;
  }
  .contact__line {
    display: flex;
    justify-content: space-between;
    align-items: baseline;
    font-size: 30px;
    line-height: 1;
    white-space: nowrap;
  }
  .contact__name {
    font-weight: 500;
    color: var(--name-ink);
    letter-spacing: 0.5px;
    text-transform: uppercase;
  }
  .contact__phone {
    font-weight: 300;
    color: var(--detail-ink);
    letter-spacing: 0.5px;
  }
  .contact__email {
    display: block;
    margin-top: 22px;
    font-size: 33px;
    font-weight: 300;
    line-height: 1;
    letter-spacing: 0.3px;
    color: var(--detail-ink);
    white-space: nowrap;
  }
</style>
</head>
<body>
  <div class="card">
    <div class="card__pattern" role="img" aria-label="Repeating pattern of small dark crosses across the charcoal card background"></div>
    <div class="card__panel">
      <h1 class="brand-name">Cedar Lodge</h1>
      <div class="contact">
        <div class="contact__rule"></div>
        <div class="contact__line">
          <span class="contact__name">Tess Varlowe</span>
          <span class="contact__phone">043 820 75 19</span>
        </div>
        <span class="contact__email">tess.varlowe@varlowe.com.au</span>
      </div>
    </div>
  </div>
</body>
</html>
```